Letterhead creation for military law attorney

I need letterhead design for my business. We are now only doing military law and need to change address, logo and vision. I like the idea of using an eagle or a jolly roger flag

Target Market(s)

Military Law Clients

Colors
3176b5
85abd2

Requirements
Must have
• We are defending people against the government
Nice to have
• Jolly Roger Flag

```html
<!DOCTYPE html>
<html lang="en">
<head>
<meta charset="utf-8">
<title>Harwell Law, PLLC – Letterhead</title>
<link rel="stylesheet" href="https://fonts.googleapis.com/css2?family=Source+Sans+3:wght@400;600;700&display=swap">
<style>
  :root {
    --brand-blue: #3176b5;
    --brand-light: #85abd2;
    --ink: #4a4a4a;
    --paper: #ffffff;
    --backdrop: #e6e6e6;
  }
  * { box-sizing: border-box; margin: 0; padding: 0; }
  html, body {
    width: 1200px;
    height: 1200px;
    overflow: hidden;
    background: var(--backdrop);
    font-family: "Source Sans 3", "Myriad Pro", sans-serif;
  }
  .letterhead {
    position: absolute;
    left: 200px;
    top: 34px;
    width: 800px;
    height: 1131px;
    background: var(--paper);
    color: var(--ink);
  }
  .masthead {
    position: absolute;
    left: 0;
    top: 0;
    width: 800px;
    height: 190px;
  }
  .masthead-rules { position: absolute; left: 0; top: 0; }
  .firm-name {
    position: absolute;
    left: 0;
    top: 132px;
    width: 800px;
    text-align: center;
    font-size: 34px;
    font-weight: 600;
    letter-spacing: 1px;
    color: var(--brand-blue);
    text-transform: uppercase;
  }
  .letter-body {
    position: absolute;
    left: 72px;
    top: 231px;
    width: 650px;
    font-size: 18px;
    line-height: 23.2px;
    hyphens: auto;
  }
  .letter-body p { margin-bottom: 23.2px; }
  .letter-body p.tight { margin-bottom: 0; }
  .signature { margin-top: 69px; }
  .footer-contact {
    position: absolute;
    left: 0;
    bottom: 30px;
    width: 800px;
    text-align: center;
    font-size: 11px;
    color: #7a7a7a;
  }
  .footer-contact strong { color: #555; font-weight: 700; }
  .footer-band {
    position: absolute;
    left: 0;
    bottom: 0;
    width: 800px;
    height: 15px;
    background: var(--brand-light);
  }
</style>
</head>
<body>
  <main class="letterhead">
    <header class="masthead">
      <svg class="masthead-rules" width="800" height="190" viewBox="0 0 800 190" aria-hidden="true">
        <line x1="62" y1="96" x2="350" y2="96" stroke="var(--brand-blue)" stroke-width="3"/>
        <line x1="450" y1="96" x2="738" y2="96" stroke="var(--brand-blue)" stroke-width="3"/>
        <circle cx="400" cy="90" r="34" fill="var(--brand-blue)"/>
      </svg>
      <div class="firm-name">Harwell Law, PLLC</div>
    </header>

    <section class="letter-body">
      <p>Dear Sir,</p>
      <p class="tight">On this good opportunity, I would like to apply as a Instrumentation and Control System Engineer in your company. My name is Dario Venn, 34 years old, male, single, energetic and healthy. I am a Control System Engineer and graduated from Eastlake Technical University (ETU) on May 2007 with GPA 3.78. I would like to have career to expand my experience.</p>
      <p>My personality as a hard worker and fast learner type of person would bring benefit to your company. I will be very appreciated if you could give in opportunity to work in your company.</p>
      <p class="tight">Herewith I enclose my curriculum vitae, which will give details of my qualification.</p>
      <p>I hope my qualifications and experience merit your consideration and look forward to your reply.</p>
      <p class="tight">Sincerely yours,</p>
      <p class="signature tight">Dario Venn<br>Email : dvenn@example.com</p>
    </section>

    <footer>
      <div class="footer-contact"><strong>PO BOX</strong> 312 Millbrook, TN 37010 &nbsp;-&nbsp; <strong>Phone</strong> (555) 014 - 2270 &nbsp;-&nbsp; <strong>FAX</strong> (555) 014 - 2271</div>
      <div class="footer-band"></div>
    </footer>
  </main>
</body>
</html>
```